Convention Display

We need a convention booth design for an 10' W x 8' T booth. It should match the look and feel of our website and our brochure design. Sample design and text via 'upload files' below. www.fernmoorhaven.com

```html
<!DOCTYPE html>
<html lang="en">
<head>
<meta charset="utf-8">
<title>Fernmoor Haven – Convention Display</title>
<link href="https://fonts.googleapis.com/css2?family=Open+Sans:wght@400;600;700&display=swap" rel="stylesheet">
<style>
  :root {
    --page-bg: #e4e5e6;
    --banner-bg: #ffffff;
    --ink-dark: #464b50;
    --band-grey: #e6e7e8;
    --label-bar: #4a4f55;
    --accent-green: #7cb526;
    --accent-blue: #1c6fb6;
    --accent-orange: #e8861f;
    --photo-light: #d9d9d9;
    --photo-dark: #8a8a8a;
  }
  html, body {
    margin: 0;
    padding: 0;
    width: 1200px;
    height: 624px;
    overflow: hidden;
    background: var(--page-bg);
  }
  .booth-banner {
    position: absolute;
    left: 210px;
    top: 24px;
    width: 780px;
    height: 576px;
    box-shadow: 0 2px 10px rgba(0,0,0,0.15);
  }
  .brand-name { font-family: "Open Sans", sans-serif; font-weight: 700; fill: var(--ink-dark); }
  .tagline { font-family: "Open Sans", sans-serif; font-weight: 400; fill: var(--ink-dark); }
  .headline { font-family: "Open Sans", sans-serif; font-weight: 700; fill: var(--ink-dark); }
  .panel-label { font-family: "Open Sans", sans-serif; font-weight: 400; fill: #ffffff; }
  .benefit { font-family: "Open Sans", sans-serif; font-weight: 400; fill: #2e3236; }
  .closing { font-family: "Open Sans", sans-serif; font-weight: 700; }
  .url { font-family: "Open Sans", sans-serif; font-weight: 400; fill: var(--ink-dark); }
</style>
</head>
<body>
<svg class="booth-banner" viewBox="0 0 616 455" xmlns="http://www.w3.org/2000/svg">
  <defs>
    <linearGradient id="photo-tone" x1="0" y1="0" x2="1" y2="1">
      <stop offset="0" stop-color="var(--photo-light)"/>
      <stop offset="1" stop-color="var(--photo-dark)"/>
    </linearGradient>
  </defs>

  <rect class="banner-bg" width="616" height="455" fill="var(--banner-bg)"/>

  <!-- header -->
  <text class="brand-name" x="20" y="53" font-size="36" textLength="283" lengthAdjust="spacingAndGlyphs">fernmoor haven</text>
  <text class="tagline" x="375" y="49" font-size="17" textLength="170" lengthAdjust="spacingAndGlyphs">connect + share + learn</text>
  <path class="header-arrow" d="M566 44 q8 -10 18 -6 l-2 -5 8 7 -9 4 2 -4 q-9 -3 -17 4z" fill="var(--ink-dark)"/>

  <!-- headline band -->
  <polygon class="headline-band" points="110,76 616,76 616,117 98,117" fill="var(--band-grey)"/>
  <text class="headline" x="128" y="103" font-size="15" textLength="469" lengthAdjust="spacingAndGlyphs">The sticky approach to web and mobile patient engagement</text>

  <!-- photo panels -->
  <g role="img" aria-label="Photo: woman holding a tablet in a bright kitchen">
    <polygon points="0,128 195,128 178,300 0,300" fill="url(#photo-tone)"/>
  </g>
  <g role="img" aria-label="Photo: hand tapping a tablet screen">
    <polygon points="205,128 400,128 383,300 188,300" fill="url(#photo-tone)"/>
  </g>
  <g role="img" aria-label="Photo: woman gesturing while holding a tablet">
    <polygon points="410,128 616,128 616,300 393,300" fill="url(#photo-tone)"/>
  </g>

  <!-- panel labels -->
  <polygon points="0,128 160,128 158,148 0,148" fill="var(--label-bar)"/>
  <text class="panel-label" x="16" y="144" font-size="14.5">make it personal</text>
  <polygon points="215,128 370,128 368,148 213,148" fill="var(--label-bar)"/>
  <text class="panel-label" x="226" y="144" font-size="14.5">make it shared</text>
  <polygon points="432,128 570,128 568,148 430,148" fill="var(--label-bar)"/>
  <text class="panel-label" x="440" y="144" font-size="14.5">make it relevant</text>

  <!-- plain markers -->
  <circle class="panel-marker" cx="173" cy="150" r="27" fill="var(--accent-green)" stroke="#fff" stroke-width="3"/>
  <circle class="panel-marker" cx="386" cy="150" r="27" fill="var(--accent-blue)" stroke="#fff" stroke-width="3"/>
  <circle class="panel-marker" cx="587" cy="150" r="27" fill="var(--accent-orange)" stroke="#fff" stroke-width="3"/>

  <!-- benefits -->
  <g class="benefit" font-size="12">
    <circle cx="167" cy="325" r="2.5" fill="#2e3236"/><text x="177" y="329">Improve satisfaction</text>
    <circle cx="160" cy="348" r="2.5" fill="#2e3236"/><text x="170" y="352">Integrate your PHR</text>
    <circle cx="153" cy="371" r="2.5" fill="#2e3236"/><text x="163" y="375">Streamline care</text>

    <circle cx="317" cy="325" r="2.5" fill="#2e3236"/><text x="327" y="329">Meet meaningful use</text>
    <circle cx="310" cy="348" r="2.5" fill="#2e3236"/><text x="320" y="352">Increase donations</text>
    <circle cx="303" cy="371" r="2.5" fill="#2e3236"/><text x="313" y="375">Incorporate staff</text>

    <circle cx="472" cy="325" r="2.5" fill="#2e3236"/><text x="482" y="329">Change behavior</text>
    <circle cx="465" cy="348" r="2.5" fill="#2e3236"/><text x="475" y="352">Capture analytics</text>
    <circle cx="458" cy="371" r="2.5" fill="#2e3236"/><text x="468" y="375">Grow your community</text>
  </g>

  <!-- closing line -->
  <text class="closing" x="33" y="421" font-size="21" textLength="305" lengthAdjust="spacingAndGlyphs"><tspan fill="var(--accent-green)" font-style="italic">3 LAYERS</tspan><tspan fill="var(--ink-dark)" dx="10">TO ENGAGEMENT</tspan></text>
  <text class="url" x="591" y="420" font-size="17" text-anchor="end">www.fernmoorhaven.com</text>
</svg>
</body>
</html>
```